Your Ridgeview Homefinder Website Design

Creative Brief: Website Design for Your Ridgeview Homefinder
- Project Overview: Design a website for our new brand, "Your Ridgeview Homefinder". Your Ridgeview Homefinder is a service that matches clients with the perfect realtor. The primary function of this site is to serve as a lead generation hub, to generate leads of people who are looking to either buy or sell their house and need a great realtor. The site needs to have a very clean, modern design using sites like Quillmark, Lumhaven, Trevista, and Pravlo as an example. The site also needs to have a primary lead capture capability through a multi-step form or questionnaire that indicates if they are buying or selling, and depending on that selection, creates two different flows.

Target Audience:
- Homebuyers and sellers in the Denver area
- Individuals looking for high-quality realtor services
- Users seeking a seamless and professional online & home buying/selling experience

Objectives:
- Create a visually appealing, modern website with a strong emphasis on lead generation.
- Design advanced, multi-step forms for efficient lead capture.
- Ensure the website is user-friendly and optimized for both desktop and mobile devices.

Pages to Design:
Home Page:
- Engaging hero section with a clear call to action and the ability to enter the form flow
- Brief introduction to Your Ridgeview Homefinder and its unique value proposition
- Key features & benefits of being matched with a realtor by Your Ridgeview Homefinder
- Testimonials and success stories
- Lead capture form

About Page:
- Overview of Your Ridgeview Homefinder’s mission and values
- Professional and trust-building imagery

How it Works Page:
- Step-by-step explanation of the matching process (complete the form and we will match you with a realtor)
- Visual aids (icons, graphics) to simplify complex information
- Customer journey map from inquiry to successful match & sale of home
- Lead capture form

Contact Us Page:
- Simple and accessible contact form
- Contact details
- Call to action for immediate inquiries

Blog Template:
- Clean, easy-to-read layout for blog posts, primarily location/neighborhood guides as well as standard blogs
- Sidebar for recent posts, categories, and tags
- Social sharing buttons
- Lead capture form embedded within blog posts

Design Style:
- Modern and professional with a focus on usability
- Clean lines and intuitive navigation
- Use of curved corners and minimal straight lines for a sleek look
- Incorporation of graphic design elements, potentially including 3D and isomorphic design
- Inspired by sites like Quillmark, Lumhaven, Trevista, and Pravlo
Consistent color scheme and typography

Visual References:
- Quillmark: For its professional and corporate look
- Lumhaven and Trevista: For their user-friendly interfaces and modern design
- Pravlo: For its clean and functional layout

Target Market(s)

- Homebuyers and sellers in the Denver area, Individuals looking for high-quality realtor services, Users seeking a seamless and professional home buying/selling experience

Industry/Entity Type

Real Estate

Number of Pages Required

5+ page

Requirements
Must have
• Fully designed website with lead capture functionality based on brief
Nice to have
• Designed in Figma, Starting / Placeholder copy

```html
<!DOCTYPE html>
<html lang="en">
<head>
<meta charset="utf-8">
<title>Your Ridgeview Homefinder</title>
<link href="https://fonts.googleapis.com/css2?family=Outfit:wght@500;600;700&family=Inter:wght@400;500;600&display=swap" rel="stylesheet">
<style>
:root{
  --green:#2a6a53;
  --green-dark:#225a46;
  --ink:#2b2b2b;
  --body:#3a3a3a;
  --bar:#3b3b3b;
  --footer:#4b4b4b;
  --white:#ffffff;
  --line:#9a9a9a;
}
*{box-sizing:border-box;margin:0;padding:0}
html,body{width:1200px;height:3886px;overflow:hidden;background:var(--white)}
body{position:relative;font-family:"Inter",Arial,sans-serif;color:var(--body)}
.abs{position:absolute}
h1,h2,h3{font-family:"Outfit",Arial,sans-serif}
.brand{display:flex;align-items:center;gap:8px;color:var(--white);font-size:14px;font-weight:500}
.brand-mark{width:14px;height:14px;border-radius:50%;background:var(--white)}

/* hero */
.hero{left:0;top:0;width:1200px;height:578px;background:var(--green)}
.nav a{position:absolute;top:47px;color:var(--white);font-size:14px;text-decoration:none}
.hero-title{left:60px;top:160px;color:var(--white);font-size:32px;font-weight:700}
.hero-text{left:60px;top:222px;width:430px;padding-left:22px;border-left:1px solid rgba(255,255,255,.6);color:var(--white);font-size:14.5px;line-height:18px}
.btn{position:absolute;display:flex;align-items:center;justify-content:center;font-size:14.5px;font-weight:500}
.btn-solid-light{background:var(--white);color:var(--green)}
.btn-ghost-light{border:1.5px solid var(--white);color:var(--white)}
.hero-photo{left:622px;top:151px;width:511px;height:303px;background:linear-gradient(180deg,#2d4660 0%,#5a5140 45%,#1f86b0 75%,#7b8a90 100%)}

/* search */
.search{left:88px;top:530px;width:1024px;height:98px;background:var(--bar);color:var(--white)}
.field{position:absolute;top:28px}
.field b{display:block;font-size:14.5px;font-weight:600;margin-bottom:9px}
.field span{font-size:11px;color:#ddd;display:flex;align-items:center;gap:10px}
.field span svg{width:12px;height:8px}
.divider{position:absolute;top:28px;width:1px;height:44px;background:#bbb}
.search-btn{left:822px;top:27px;width:175px;height:51px;background:var(--white);color:var(--green)}

/* about */
.about-photo{left:68px;top:693px;width:519px;height:484px;background:linear-gradient(180deg,#9cc0df 0%,#d9e4ee 40%,#4b7596 60%,#3f6b3c 85%,#cfcfcf 100%)}
.about-title{left:659px;top:696px;color:var(--green);font-size:31px;font-weight:700}
.about-text{left:662px;top:744px;width:460px;height:358px;padding-left:24px;border-left:1px solid var(--line);font-size:14.5px;line-height:18px}
.about-text p+p{margin-top:36px}
.btn-solid{background:var(--green);color:var(--white)}

/* how it works */
.section-title{left:0;width:1200px;text-align:center;color:var(--green);font-size:31px;font-weight:700}
.step-label{font-size:15px;font-weight:700;color:var(--ink);font-family:"Outfit",Arial,sans-serif}
.step-sub{font-size:14.5px;font-weight:600;color:var(--green)}
.step-text{width:430px;padding-left:18px;border-left:1px solid var(--line);font-size:14.5px;line-height:18px}
.illus{border-radius:6px;background:linear-gradient(135deg,#eef3f0,#cfe0d7 60%,#2a6a53 140%)}

/* browse */
.browse-title{left:47px;top:2586px;font-size:16px;font-weight:600;color:var(--ink)}
.tile{position:absolute;width:267px;height:183px;border-radius:4px;overflow:hidden}
.tile b{position:absolute;left:20px;top:20px;color:var(--white);font-size:16px;font-weight:500}
.tile i{position:absolute;right:20px;bottom:16px;width:52px;height:26px;border-radius:13px;background:var(--white);color:var(--green);font-style:normal;font-size:15px;font-weight:600;display:flex;align-items:center;justify-content:center}

/* blogs */
.blogs{left:0;top:3061px;width:1200px;height:410px;background:var(--green)}
.blog-card{position:absolute;top:3146px;width:231px;height:279px;background:var(--white)}
.blog-card .pic{position:absolute;left:15px;top:15px;width:201px;height:118px}
.blog-card h3{position:absolute;left:15px;top:153px;width:201px;display:flex;justify-content:space-between;font-family:"Inter",Arial,sans-serif;font-size:14.5px;font-weight:600;color:var(--green)}
.blog-card h3 span{color:var(--ink)}
.blog-card p{position:absolute;left:15px;top:192px;width:140px;font-size:14px;line-height:17px}
.blog-card svg{position:absolute;right:16px;bottom:18px}

/* footer */
.footer{left:0;top:3471px;width:1200px;height:347px;background:var(--footer);color:var(--white)}
.col-head{position:absolute;font-size:12.5px;font-weight:600;padding-left:22px}
.col-head::before{content:"";position:absolute;left:0;top:-4px;width:1.5px;height:22px;background:var(--white)}
.f-item{position:absolute;font-size:13px;line-height:16px;padding-left:28px}
.f-item::before{content:"›";position:absolute;left:0;top:-1px;font-size:15px}
.social{position:absolute;top:3596px;width:30px;height:30px;border-radius:50%;background:var(--white)}
.legal{left:0;top:3818px;width:1200px;height:68px;font-size:15px;color:var(--green)}
</style>
</head>
<body>

<!-- hero -->
<section class="abs hero">
  <div class="abs brand" style="left:50px;top:40px"><span class="brand-mark"></span>Your Ridgeview Homefinder</div>
  <nav class="nav">
    <a style="left:620px" href="#">Home</a>
    <a style="left:717px" href="#">About us</a>
    <a style="left:835px" href="#">How it’s Work</a>
    <a style="left:986px" href="#">Blogs</a>
    <a style="left:1080px" href="#">Contact</a>
  </nav>
  <h1 class="abs hero-title">Looking for a dream home?</h1>
  <p class="abs hero-text">Lorem ipsum dolor sit amet, consectetuer adipiscing elit, sed diam nonummy nibh euismod tincidunt ut laoreet dolore magna aliquam erat volutpat.Lorem ipsum dolor sit amet, consectetuer adipiscing elit, sed diam nonummy nibh euismod tincidunt ut laoreet dolore magna</p>
  <a class="btn btn-solid-light" style="left:60px;top:389px;width:175px;height:52px">Get Started</a>
  <a class="btn btn-ghost-light" style="left:264px;top:389px;width:175px;height:52px">Read More</a>
  <div class="abs hero-photo" role="img" aria-label="Luxury villa with lit pool at dusk"></div>
</section>

<!-- search bar -->
<form class="abs search">
  <div class="field" style="left:30px"><b>Buy a House</b><span>Select Your City <svg viewBox="0 0 12 8"><path d="M1 1l5 5 5-5" fill="none" stroke="#fff" stroke-width="1.5"/></svg></span></div>
  <div class="divider" style="left:192px"></div>
  <div class="field" style="left:220px"><b>Sell a House</b><span>Select &nbsp;Your City <svg viewBox="0 0 12 8"><path d="M1 1l5 5 5-5" fill="none" stroke="#fff" stroke-width="1.5"/></svg></span></div>
  <div class="divider" style="left:392px"></div>
  <div class="field" style="left:417px"><b>Locations</b><span>Select Your City <svg viewBox="0 0 12 8"><path d="M1 1l5 5 5-5" fill="none" stroke="#fff" stroke-width="1.5"/></svg></span></div>
  <div class="divider" style="left:573px"></div>
  <div class="field" style="left:601px"><b>Property type</b><span>Select Property type <svg viewBox="0 0 12 8"><path d="M1 1l5 5 5-5" fill="none" stroke="#fff" stroke-width="1.5"/></svg></span></div>
  <div class="divider" style="left:787px"></div>
  <a class="btn search-btn">Search</a>
</form>

<!-- about -->
<div class="abs about-photo" role="img" aria-label="Glass office towers under a cloudy sky"></div>
<h2 class="abs about-title">About us</h2>
<div class="abs about-text">
  <p>Lorem ipsum dolor sit amet, consectetuer adipiscing elit, sed diam nonummy nibh euismod tincidunt ut laoreet dolore magna aliquam erat volutpat. Ut wisi enim ad minim veniam, quis nostrud exerci tation ullamcorper suscipit lobortis nisl ut aliquip ex ea commodo consequat.</p>
  <p>Lorem ipsum dolor sit amet, consectetuer adipiscing elit, sed diam nonummy nibh euismod tincidunt ut laoreet dolore magna aliquam erat volutpat. Ut wisi enim ad minim veniam, quis nostrud exerci tation ullamcorper suscipit lobortis nisl ut aliquip ex ea commodo consequat. Duis autem vel eum iriure dolor in hendrerit in vulputate velit esse molestie consequat, vel illum dolore eu feugiat nulla facilisis at vero eros et accumsan et iusto odio dignissim qui blandit praesent luptatum zzril delenit augue duis dolore te feugait nulla facilisi.</p>
</div>
<a class="btn btn-solid" style="left:661px;top:1126px;width:175px;height:51px">Read More</a>

<!-- how it works -->
<h2 class="abs section-title" style="top:1245px">How it’s Work</h2>

<svg class="abs" style="left:0;top:0" width="1200" height="2600" viewBox="0 0 1200 2600" fill="none">
  <g stroke="#555" stroke-width="1.4" stroke-dasharray="10 7">
    <path d="M257 1338H558V1558"/>
    <path d="M539 1594H324"/>
    <path d="M257 1751V1813"/>
    <path d="M282 1838H685V2011"/>
    <path d="M661 2034H257V2097"/>
    <path d="M257 2264V2316"/>
  </g>
  <g stroke="var(--green)" stroke-width="1.6">
    <circle cx="557" cy="1578" r="18" fill="#fff"/><path d="M550 1571l13 13m0-8v8h-8"/>
    <circle cx="261" cy="1832" r="18" fill="#fff"/><path d="M254 1833l5 5 10-11"/>
    <circle cx="682" cy="2030" r="18" fill="#fff"/><path d="M675 2023l13 13m0-8v8h-8"/>
  </g>
  <circle cx="161" cy="1346" r="12" fill="var(--green)"/><path d="M155 1346l4 4 8-8" stroke="#fff" stroke-width="2"/>
  <circle cx="771" cy="1589" r="12" fill="#333"/>
  <circle cx="161" cy="1827" r="12" fill="#333"/>
  <circle cx="777" cy="2093" r="12" fill="#333"/>
  <circle cx="161" cy="2333" r="12" fill="#333"/>
</svg>

<div class="abs step-label" style="left:69px;top:1339px">Step 01</div>
<div class="abs step-sub" style="left:69px;top:1368px">Get your home valuation</div>
<p class="abs step-text" style="left:72px;top:1401px">Lorem ipsum dolor sit amet, consectetuer adipiscing elit, sed diam nonummy nibh euismod tincidunt ut laoreet dolore magna aliquam erat volutpat. Ut wisi enim ad minim veniam, quis nostrud exerci tation ullamcorper suscipit lobortis nisl ut aliquip ex ea commodo consequat.</p>
<div class="abs illus" style="left:732px;top:1373px;width:256px;height:181px" role="img" aria-label="Illustration of agent and client shaking hands over a scale"></div>
<div class="abs illus" style="left:116px;top:1562px;width:208px;height:189px" role="img" aria-label="Illustration of a team reviewing a home valuation on a screen"></div>

<div class="abs step-label" style="left:679px;top:1580px">Step 02</div>
<div class="abs step-sub" style="left:679px;top:1610px">Meet your agent</div>
<p class="abs step-text" style="left:682px;top:1643px">Lorem ipsum dolor sit amet, consectetuer adipiscing elit, sed diam nonummy nibh euismod tincidunt ut laoreet dolore magna aliquam erat volutpat. Ut wisi enim ad minim veniam, quis nostrud exerci tation ullamcorper suscipit lobortis nisl ut aliquip ex ea commodo consequat.</p>

<div class="abs step-label" style="left:69px;top:1818px">Step 03</div>
<div class="abs step-sub" style="left:69px;top:1848px">Choose your services</div>
<p class="abs step-text" style="left:72px;top:1882px">Lorem ipsum dolor sit amet, consectetuer adipiscing elit, sed diam nonummy nibh euismod tincidunt ut laoreet dolore magna aliquam erat volutpat. Ut wisi enim ad minim veniam, quis nostrud exerci tation ullamcorper suscipit lobortis nisl ut aliquip ex ea commodo consequat.</p>
<div class="abs illus" style="left:773px;top:1830px;width:200px;height:192px" role="img" aria-label="Illustration of a couple choosing a home on a phone screen"></div>

<div class="abs step-label" style="left:685px;top:2085px">Step 04</div>
<div class="abs step-sub" style="left:685px;top:2115px">Log in</div>
<p class="abs step-text" style="left:688px;top:2148px">Lorem ipsum dolor sit amet, consectetuer adipiscing elit, sed diam nonummy nibh euismod tincidunt ut laoreet dolore magna aliquam erat volutpat. Ut wisi enim ad minim veniam, quis nostrud exerci tation ullamcorper suscipit lobortis nisl ut aliquip ex ea commodo consequat.</p>
<div class="abs illus" style="left:151px;top:2097px;width:158px;height:167px" role="img" aria-label="Illustration of a person logging in on a large phone"></div>

<div class="abs step-label" style="left:69px;top:2324px">Step 05</div>
<div class="abs step-sub" style="left:69px;top:2355px">Actually enjoy closing</div>
<p class="abs step-text" style="left:72px;top:2386px">Lorem ipsum dolor sit amet, consectetuer adipiscing elit, sed diam nonummy nibh euismod tincidunt ut laoreet dolore magna aliquam erat volutpat. Ut wisi enim ad minim veniam, quis nostrud exerci tation ullamcorper suscipit lobortis nisl ut aliquip ex ea commodo consequat.</p>
<div class="abs illus" style="left:735px;top:2339px;width:268px;height:173px" role="img" aria-label="Illustration of people relaxing at home with laptops"></div>

<!-- browse -->
<h3 class="abs browse-title">Browse Home in America</h3>
<div class="tile" style="left:47px;top:2630px;background:linear-gradient(180deg,#4a4d5a,#7a4a32 60%,#2a2a30)" role="img" aria-label="Modern house lit at night"><b>New Listing</b><i>234</i></div>
<div class="tile" style="left:326px;top:2630px;background:linear-gradient(180deg,#6f8ea8,#a8a18a 55%,#4f7a3a)" role="img" aria-label="Suburban family house with lawn"><b>Price reduce</b><i>434</i></div>
<div class="tile" style="left:605px;top:2630px;background:linear-gradient(180deg,#6c7a8a,#d8d0c2 55%,#2f7fa0)" role="img" aria-label="White mansion with pool"><b>Open Houses</b><i>134</i></div>
<div class="tile" style="left:884px;top:2630px;background:linear-gradient(180deg,#8aa0b0,#c9cfcf 50%,#3f5a44)" role="img" aria-label="Contemporary multi-storey residence"><b>Recently Sold</b><i>934</i></div>
<div class="tile" style="left:47px;top:2828px;background:linear-gradient(180deg,#8fa4b8,#7a6a55 55%,#b0874a)" role="img" aria-label="New apartment complex with playground"><b>New Construction</b><i>734</i></div>
<div class="tile" style="left:326px;top:2828px;background:linear-gradient(180deg,#a9b6c0,#d6d8d6 50%,#4f7a3a)" role="img" aria-label="White two-storey home among trees"><b>New Home Communities</b><i>634</i></div>
<div class="tile" style="left:605px;top:2828px;background:linear-gradient(180deg,#7c8d9c,#c8c6bf 50%,#2b7ea0)" role="img" aria-label="Modern villa beside a pool"><b>Land</b><i>734</i></div>
<div class="tile" style="left:884px;top:2828px;background:linear-gradient(180deg,#3d5a38,#8a7a66 55%,#3f5f30)" role="img" aria-label="Stone house surrounded by trees"><b>Condos</b><i>434</i></div>

<!-- blogs -->
<section class="abs blogs">
  <h2 class="abs section-title" style="top:38px;color:var(--white)">Blogs</h2>
  <svg class="abs" style="left:58px;top:208px" width="16" height="24" viewBox="0 0 16 24"><path d="M12 2L3 12l9 10" fill="none" stroke="#fff" stroke-width="1.8"/></svg>
  <svg class="abs" style="left:1126px;top:208px" width="16" height="24" viewBox="0 0 16 24"><path d="M4 2l9 10-9 10" fill="none" stroke="#fff" stroke-width="1.8"/></svg>
</section>
<article class="blog-card" style="left:122px"><div class="pic" role="img" aria-label="Modern house with pool at night" style="background:linear-gradient(180deg,#2a3a3a,#6a4a30 55%,#1d5f7a)"></div><h3>Lorem ipsum <span>6min</span></h3><p>Lorem ipsum dolor sit amet, consectetuer adipiscing elit</p><svg width="36" height="36" viewBox="0 0 36 36"><circle cx="18" cy="18" r="17" fill="none" stroke="#2a6a53" stroke-width="1.5"/><path d="M12 12l12 12m0-8v8h-8" fill="none" stroke="#2a6a53" stroke-width="1.5"/></svg></article>
<article class="blog-card" style="left:365px"><div class="pic" role="img" aria-label="Villa with lit pool at dusk" style="background:linear-gradient(180deg,#2d4660,#5a5140 50%,#1f86b0)"></div><h3>Lorem ipsum <span>6min</span></h3><p>Lorem ipsum dolor sit amet, consectetuer adipiscing elit</p><svg width="36" height="36" viewBox="0 0 36 36"><circle cx="18" cy="18" r="17" fill="none" stroke="#2a6a53" stroke-width="1.5"/><path d="M12 12l12 12m0-8v8h-8" fill="none" stroke="#2a6a53" stroke-width="1.5"/></svg></article>
<article class="blog-card" style="left:608px"><div class="pic" role="img" aria-label="Modern house lit at night" style="background:linear-gradient(180deg,#4a4d5a,#7a4a32 60%,#2a2a30)"></div><h3>Lorem ipsum <span>6min</span></h3><p>Lorem ipsum dolor sit amet, consectetuer adipiscing elit</p><svg width="36" height="36" viewBox="0 0 36 36"><circle cx="18" cy="18" r="17" fill="none" stroke="#2a6a53" stroke-width="1.5"/><path d="M12 12l12 12m0-8v8h-8" fill="none" stroke="#2a6a53" stroke-width="1.5"/></svg></article>
<article class="blog-card" style="left:850px"><div class="pic" role="img" aria-label="Suburban house with garden" style="background:linear-gradient(180deg,#6f8ea8,#c8c2b2 55%,#4f7a3a)"></div><h3>Lorem ipsum <span>6min</span></h3><p>Lorem ipsum dolor sit amet, consectetuer adipiscing elit</p><svg width="36" height="36" viewBox="0 0 36 36"><circle cx="18" cy="18" r="17" fill="none" stroke="#2a6a53" stroke-width="1.5"/><path d="M12 12l12 12m0-8v8h-8" fill="none" stroke="#2a6a53" stroke-width="1.5"/></svg></article>

<!-- footer -->
<footer class="abs footer">
  <div class="abs brand" style="left:63px;top:90px;font-size:16px"><span class="brand-mark"></span>Your Ridgeview Homefinder</div>
  <p class="abs" style="left:64px;top:170px;width:300px;font-size:14px;line-height:17px">Lorem ipsum dolor sit amet, consectetuer adipiscing elit, sed diam nonummy nibh euismod tincidunt ut laoreet dolore magna aliquam erat volutpat. Ut wisi enim ad minim veniam</p>

  <div class="col-head" style="left:418px;top:81px">Our Office</div>
  <div class="f-item" style="left:415px;top:128px">(1) 555-014-2278</div>
  <div class="f-item" style="left:415px;top:183px">48 Aspen Hollow Lane Suite 12,<br>Ridgeview 80421</div>
  <div class="f-item" style="left:415px;top:249px">yourridgeviewhomefinder.com</div>

  <div class="col-head" style="left:729px;top:81px">Quick link</div>
  <div class="f-item" style="left:726px;top:123px">Home</div>
  <div class="f-item" style="left:726px;top:158px">Service</div>
  <div class="f-item" style="left:726px;top:191px">How it’s Work</div>
  <div class="f-item" style="left:726px;top:226px">Blogs</div>
  <div class="f-item" style="left:726px;top:259px">Contact</div>

  <div class="col-head" style="left:934px;top:81px">Connect with</div>
  <div class="col-head" style="left:934px;top:200px">Subscribe For News Letter</div>
  <div class="abs" style="left:936px;top:243px;width:157px;height:30px;background:#fff;color:#999;font-size:11px;padding:9px 16px">Enter your mail</div>
  <svg class="abs" style="left:1093px;top:243px" width="39" height="30" viewBox="0 0 39 30"><rect width="39" height="30" fill="#2a6a53"/><path d="M11 15h17m-5-5l5 5-5 5" fill="none" stroke="#fff" stroke-width="1.6"/></svg>
</footer>
<span class="social" style="left:933px" aria-label="Social profile"></span>
<span class="social" style="left:976px" aria-label="Social profile"></span>
<span class="social" style="left:1017px" aria-label="Social profile"></span>
<span class="social" style="left:1060px" aria-label="Social profile"></span>

<div class="abs legal">
  <span class="abs" style="left:68px;top:23px">2024 all rights reserved</span>
  <span class="abs" style="left:850px;top:23px">Privacy policy</span>
  <span class="abs" style="left:976px;top:18px;width:2px;height:26px;background:var(--green)"></span>
  <span class="abs" style="left:1000px;top:23px">Terms &amp; Conditions</span>
</div>

</body>
</html>
```